Flyer für ein Singer-Songwriter Festival
Vielen Dank für die Geduld und die schnellen Änderungen. Ich bin sehr zufrieden mit dem Ergebnis und freue mich auf die weitere Zusammenarbeit!
Zielgruppe
Wir sind ein gemeinnütziger Verein und unterstützen Kunst und Kulturschafende. Im November veranstalten wir ein Singer-Songwriter Festival. Es heißt: TideLark Korven Folkwave Festival. Im letzten Jahr fand das erste Festival statt und richtet sich an Newcommer aus Der Bereich Singer Songwriter und Kulturliebhaber bzw. Festivalgänger
Das Festival findet vom 28. November bis 29. November 2025 statt. Am ersten Abend findet der Contest der Newcomer statt der zweite Abend ist der 'Konzertabend' an dem die Jury und der / die Gewinnerin des Contest den Abend mit bestreiten werden.
Diese Informationen sollten auf die Rückseite des Flyers. Der Button 'Wir suchen dich' sollte ebenfalls auf die Rückseite.
ICON Pixora & Chatterly bitte einfügen.
Gefördert wird das Festival von der TULPA-Stiftung und der Konrad Wessel & Ida Marquardt-Stiftung (Varnek) dies sollte auf dem Flyer erwähnt werden
Aufgabenstellung
Ansprechend für junge Leute. Es gibt ein Logo und auch ein gestaltetes Plakat aus dem letzten Jahr. Postkartengröße für den Flyer.
DINA 4 Plakate

```html
<!DOCTYPE html>
<html lang="de">
<head>
<meta charset="utf-8">
<title>TideLark Korven Folkwave – Flyer</title>
<link href="https://fonts.googleapis.com/css2?family=Bebas+Neue&family=Montserrat:wght@600;800&display=swap" rel="stylesheet">
<style>
  :root {
    --page-bg: #e8e8e8;
    --sand: #f3bd62;
    --sand-deep: #e3a94f;
    --accent-red: #e0573a;
    --slate: #3f4d58;
    --badge-grey: #a9b4b3;
    --ink: #1c1a19;
    --shadow-brown: #2d201b;
    --mid-brown: #7a5634;
    --band-white: #f3f3f3;
    --coin-silver: #d9d9d9;
    --white: #ffffff;
  }
  * { box-sizing: border-box; margin: 0; padding: 0; }
  html, body { width: 1200px; height: 1200px; overflow: hidden; }
  body { background: var(--page-bg); position: relative; font-family: "Montserrat", sans-serif; }

  .flyer {
    position: absolute; left: 200px; top: 34px;
    width: 800px; height: 1131px;
    background: var(--sand);
    overflow: hidden;
  }
  .flyer__texture {
    position: absolute; inset: 0 0 151px 0;
    background: radial-gradient(circle at 60% 35%, var(--sand) 0%, var(--sand-deep) 130%);
  }

  .event-date, .event-venue {
    position: absolute;
    font-family: "Bebas Neue", sans-serif;
    color: var(--accent-red);
    line-height: 0.95;
    text-align: center;
  }
  .event-date { left: 60px; top: 175px; font-size: 40px; }
  .event-date__month { font-size: 32px; display: block; }
  .event-date__year { font-size: 26px; display: block; }
  .event-venue { right: 70px; top: 70px; font-size: 32px; }

  .festival-mark {
    position: absolute; left: 0; right: 0; top: 250px;
    text-align: center;
  }
  .festival-mark__name {
    font-family: "Bebas Neue", sans-serif;
    font-size: 120px; line-height: 0.9;
    color: var(--slate);
    letter-spacing: 2px;
  }
  .festival-mark__tagline {
    font-weight: 600;
    font-size: 14px; letter-spacing: 6px;
    color: var(--white); text-transform: uppercase;
    margin-top: 8px;
  }
  .festival-mark__sub {
    font-family: "Bebas Neue", sans-serif;
    font-size: 64px; line-height: 1;
    color: var(--accent-red); margin-top: 6px;
  }

  .contest-badge {
    position: absolute; left: 560px; top: 430px;
    width: 190px; height: 190px; border-radius: 50%;
    background: var(--badge-grey);
    display: flex; flex-direction: column; align-items: center; justify-content: center;
    text-align: center; text-transform: uppercase;
    z-index: 2;
  }
  .contest-badge__headline { color: var(--white); font-weight: 800; font-size: 22px; line-height: 1; }
  .contest-badge__text { color: var(--slate); font-weight: 800; font-size: 10.5px; line-height: 1.2; margin-top: 8px; }

  .performers-art {
    position: absolute; left: 0; right: 0; top: 540px; height: 440px;
    background:
      radial-gradient(ellipse 200px 230px at 28% 55%, var(--shadow-brown) 0%, var(--shadow-brown) 55%, rgba(45,32,27,0) 100%),
      radial-gradient(ellipse 170px 210px at 72% 62%, var(--shadow-brown) 0%, var(--mid-brown) 55%, rgba(122,86,52,0) 100%),
      radial-gradient(ellipse 120px 150px at 45% 78%, var(--mid-brown) 0%, rgba(122,86,52,0) 100%),
      linear-gradient(180deg, rgba(45,32,27,0) 0%, rgba(45,32,27,0) 50%, var(--shadow-brown) 100%);
  }

  .info-band {
    position: absolute; left: 0; right: 0; bottom: 0; height: 151px;
    background: var(--band-white);
  }
  .partner-coin {
    position: absolute; left: 70px; top: 915px;
    width: 150px; height: 150px; border-radius: 50%;
    background: radial-gradient(circle at 40% 35%, #f4f4f4 0%, var(--coin-silver) 70%, #bdbdbd 100%);
    box-shadow: 0 4px 10px rgba(0,0,0,0.2);
  }
  .info-band__text {
    position: absolute; left: 250px; top: 1000px; width: 530px;
    font-size: 9.5px; font-weight: 800; color: var(--ink); text-transform: uppercase;
    line-height: 1.3;
  }
  .info-band__url { white-space: nowrap; }
  .info-band__social { display: flex; align-items: center; gap: 6px; margin-top: 8px; font-size: 10.5px; }
  .info-band__dot { width: 10px; height: 10px; border-radius: 50%; background: var(--sand-deep); }
  .info-band__sponsors {
    margin-top: 12px; font-weight: 600; font-size: 9.5px; text-transform: none; color: var(--slate);
  }
</style>
</head>
<body>
  <main class="flyer">
    <div class="flyer__texture" role="img" aria-label="Faint grunge texture with wavy lines in sand tones"></div>

    <div class="event-date">28 – 29<span class="event-date__month">November</span><span class="event-date__year">2025</span></div>
    <div class="event-venue">Driftwood<br>Strandholm</div>

    <div class="festival-mark">
      <div class="festival-mark__name">TideLark</div>
      <div class="festival-mark__tagline">Singer·Songwriter·Festival</div>
      <div class="festival-mark__sub">Korven Folkwave</div>
    </div>

    <div class="contest-badge">
      <div class="contest-badge__headline">Wir<br>suchen<br>dich!</div>
      <div class="contest-badge__text">Bewirb dich jetzt<br>bei unserem<br>Singer-Songwriter<br>Contest</div>
    </div>

    <div class="performers-art" role="img" aria-label="Two-tone brown illustration of three singers performing on stage, one with a microphone"></div>

    <section class="info-band"></section>
    <div class="partner-coin" role="img" aria-label="Silver partner badge of Kunstgroschen Hanseburg e.V."></div>
    <div class="info-band__text">
      <div class="info-band__url">Alle Infos unter www.kunstgroschen-hanseburg.de/tlkf-songwriterfestival</div>
      <div class="info-band__social"><span class="info-band__dot"></span>tidelarkkorvenfolkwave</div>
      <div class="info-band__sponsors">Gefördert von der TULPA-Stiftung und der Konrad Wessel &amp; Ida Marquardt-Stiftung (Varnek)</div>
    </div>
  </main>
</body>
</html>
```